dorwial business card design so that it looks better

need a new business card designed. use our website, dorwian.com for example. I attached an example of a previous card we had and liked. this is for law enforcement and we have attached a previous business card as an example. This site forces me to select color and font, ignore those as I picked stuff just to get this completed.

Target Market(s)

law enforcement, local government

Contact Information for Business Card

see the attached example and our website

Font styles to use
Serif

```html
<!DOCTYPE html>
<html lang="en">
<head>
<meta charset="utf-8">
<title>Dorwial Business Card</title>
<link href="https://fonts.googleapis.com/css2?family=Exo+2:wght@300;400&family=Raleway:wght@200&family=Roboto:ital,wght@0,300;1,300&display=swap" rel="stylesheet">
<style>
  :root {
    --page: #c4c4c4;
    --card: #03131d;
    --card-deep: #021019;
    --blue: #0a86cf;
    --band-blue: #0c69a8;
    --white: #f2f4f5;
    --muted: #d7dde1;
  }
  * { margin: 0; padding: 0; box-sizing: border-box; }
  html, body { width: 1200px; height: 576px; overflow: hidden; }
  body { background: var(--page); position: relative; font-family: "Roboto", sans-serif; }

  .card {
    position: absolute;
    background: var(--card);
    border-radius: 13px;
    overflow: hidden;
  }
  .card--front { left: 82px; top: 139px; width: 484px; height: 293px; }
  .card--back  { left: 602px; top: 138px; width: 480px; height: 291px; }

  .network-map {
    position: absolute; left: 20px; top: 15px; width: 440px; height: 250px;
    background: radial-gradient(ellipse at 50% 50%, rgba(30,70,95,0.35) 0%, rgba(15,40,58,0.2) 45%, rgba(3,19,29,0) 75%);
  }

  .wordmark {
    position: absolute;
    font-family: "Raleway", sans-serif;
    font-weight: 200;
    color: var(--white);
    letter-spacing: 0.04em;
    line-height: 1;
    white-space: nowrap;
  }
  .card--front .wordmark { left: 0; width: 100%; text-align: center; top: 100px; font-size: 60px; }
  .card--back .wordmark { left: 34px; top: 113px; font-size: 44px; }

  .band { position: absolute; bottom: 0; left: 0; }
  .front-url {
    position: absolute; left: 314px; top: 272px;
    font-size: 13px; letter-spacing: 0.28em; color: var(--muted); font-weight: 300;
  }

  .tagline {
    position: absolute; left: 34px; top: 160px;
    font-size: 10.5px; letter-spacing: 0.12em; color: var(--muted); font-weight: 300;
    white-space: nowrap;
  }
  .tagline .divider { color: #5d6b74; margin: 0 6px; }

  .contact { position: absolute; left: 280px; top: 62px; color: var(--muted); }
  .contact__name { font-family: "Exo 2", sans-serif; font-weight: 400; font-size: 21px; color: var(--blue); line-height: 1.1; }
  .contact__title { font-style: italic; font-weight: 300; font-size: 12.5px; margin-top: 4px; }
  .contact__address { font-size: 13px; font-weight: 300; line-height: 17px; margin-top: 19px; }
  .contact__list { list-style: none; margin-top: 6px; }
  .contact__list li { display: flex; align-items: center; font-size: 13px; font-weight: 300; height: 17.5px; }
  .contact__list svg { width: 11px; height: 11px; margin-right: 11px; fill: var(--blue); }
</style>
</head>
<body>
  <section class="card card--front">
    <div class="network-map" role="img" aria-label="Faint network map of the United States with connected points"></div>
    <div class="wordmark">DORWIAL</div>
    <svg class="band" width="270" height="23" viewBox="0 0 270 23" aria-hidden="true">
      <polygon points="0,0 195,0 176,23 0,23" fill="var(--band-blue)"/>
      <polygon points="208,0 270,0 258,23 196,23" fill="var(--white)"/>
    </svg>
    <div class="front-url">www.dorwian.com</div>
  </section>

  <section class="card card--back">
    <div class="wordmark">DORWIAL</div>
    <div class="tagline">Better Technology<span class="divider">|</span>Better Service</div>
    <div class="contact">
      <div class="contact__name">Marcus Hale</div>
      <div class="contact__title">Founder/Chief Exe. Officer</div>
      <div class="contact__address">4120 Linden Parkway<br>Austin, TX 78704</div>
      <ul class="contact__list">
        <li><svg viewBox="0 0 12 12" aria-hidden="true"><path d="M1 4c0-1.5 2.5-2.5 5-2.5S11 2.5 11 4v1H8.5V3.8h-5V5H1z"/><path d="M3 6h6l1.5 5h-9z"/></svg>866.555.0142</li>
        <li><svg viewBox="0 0 12 12" aria-hidden="true"><path d="M0 2.5h12v7H0z"/><path d="M0 2.5l6 4 6-4" fill="none" stroke="var(--card)" stroke-width="1"/></svg>info@dorwian.com</li>
        <li><svg viewBox="0 0 12 12" aria-hidden="true"><circle cx="6" cy="6" r="5.5"/><path d="M0.5 6h11M6 0.5v11M6 0.5c-2.5 3-2.5 8 0 11M6 0.5c2.5 3 2.5 8 0 11" fill="none" stroke="var(--card)" stroke-width="0.7"/></svg>www.dorwian.com</li>
      </ul>
    </div>
  </section>
</body>
</html>
```